Billboard to promote Harwell County, NC

I would like a billboard designed for the Chamber of Commerce. The size of the board is 10'h by 24'w. I would like our logo colors used and IF space permits, include our logo. I want to board to be very easy to read with a simplistic message of #StayWithHarwell, Invest in this community, Shop, Dine, Live. I would like our web address to scroll the bottom of the board, www.TheHarwellChamber.example

Target Market(s)

Local residents and visitors

Industry/Entity Type

Chamber Of Commerce

Requirements
Must have
• Quick message
• Easy to read
• Bold type
Nice to have
• Our logo, if space permits.
Should not have
• Should not be too busy or hard to read. People are driving by at 55-65 miles per hour.

```html
<!DOCTYPE html>
<html lang="en">
<head>
<meta charset="utf-8">
<title>Harwell Chamber Billboard</title>
<link href="https://fonts.googleapis.com/css2?family=Montserrat:wght@500;700&display=swap" rel="stylesheet">
<style>
  :root {
    --sky-mist: #c9d6de;
    --haze-blue: #7f9bab;
    --ridge-blue: #4e6a7b;
    --valley-slate: #34444f;
    --rock-grey: #6b6d6a;
    --rock-dark: #2a2f33;
    --text-white: #ffffff;
    --band: rgba(18, 30, 42, 0.6);
  }
  html, body {
    margin: 0;
    padding: 0;
    width: 1200px;
    height: 604px;
    overflow: hidden;
    background: #ffffff;
  }
  .billboard {
    position: relative;
    width: 1200px;
    height: 604px;
    overflow: hidden;
    font-family: "Montserrat", Arial, sans-serif;
    color: var(--text-white);
  }
  .scenic-backdrop {
    position: absolute;
    inset: 0;
    background:
      radial-gradient(ellipse 70% 55% at 88% 78%, rgba(120,120,114,0.75) 0%, rgba(120,120,114,0) 70%),
      radial-gradient(ellipse 60% 45% at 20% 85%, rgba(40,46,50,0.8) 0%, rgba(40,46,50,0) 75%),
      linear-gradient(180deg, var(--sky-mist) 0%, var(--haze-blue) 16%, var(--ridge-blue) 34%, var(--valley-slate) 56%, var(--rock-dark) 100%);
  }
  .hashtag {
    position: absolute;
    left: 0;
    right: 0;
    top: 100px;
    margin: 0;
    text-align: center;
    font-weight: 700;
    font-size: 112px;
    letter-spacing: -1px;
    line-height: 1.15;
    text-shadow: 0 3px 14px rgba(0,0,0,0.35);
  }
  .chamber {
    position: absolute;
    left: 0;
    right: 0;
    top: 292px;
    text-align: center;
  }
  .chamber-dot {
    display: block;
    margin: 0 auto 16px;
    width: 92px;
    height: 92px;
  }
  .chamber-name {
    margin: 0;
    font-weight: 700;
    font-size: 30px;
    line-height: 1.1;
    letter-spacing: 0.5px;
    text-transform: uppercase;
  }
  .chamber-name span {
    display: block;
    font-weight: 500;
    font-size: 17px;
    letter-spacing: 5px;
  }
  .web-band {
    position: absolute;
    left: 0;
    right: 0;
    top: 516px;
    height: 60px;
    background: var(--band);
    display: flex;
    align-items: center;
    justify-content: center;
  }
  .web-address {
    margin: 0;
    font-weight: 500;
    font-size: 29px;
    letter-spacing: 1px;
  }
</style>
</head>
<body>
  <main class="billboard">
    <div class="scenic-backdrop" role="img" aria-label="Photograph of misty blue mountain ridges fading into the distance behind rugged grey rocky peaks"></div>
    <h1 class="hashtag">#StayWithHarwell</h1>
    <div class="chamber">
      <svg class="chamber-dot" viewBox="0 0 92 92" aria-hidden="true">
        <circle cx="46" cy="46" r="40" fill="var(--text-white)"/>
      </svg>
      <p class="chamber-name">Harwell Chamber <span>of Commerce &amp; Tourism</span></p>
    </div>
    <div class="web-band">
      <p class="web-address">www.TheHarwellChamber.example</p>
    </div>
  </main>
</body>
</html>
```